Slider needed for Database Documentation Topic

We need a slider to promote a content area of a web site. I'm listing this as a poster because the posters I have seen on FrameHarbor portfolios most closely resemble the combination or art and text I am looking for.
The content area we are promoting with this graphic will clarify the design and use of a complicated database. The title of the content area is "The Kindled VQ Database" and the banner should use that title.
To 'illuminate' something means to cast light on it, and this content area will help shed light on a complicated thing – the content will use diagrams, text, and examples to clarify the database. Another meaning is that an illuminated manuscript is a manuscript brought to life with pictures, and in a way that is also what this content area will do.
One idea for the slider might be a light bulb, lamp, candle or flashlight lighting up the words "VQ Database". Another idea would be the type of illustration you see if you search for "Illuminated manuscript"
But I'm not committed to any particular idea - in the past I have been pleased to see ideas that are different than my own but accomplish the same thing, so please feel free to use your judgement or ask any questions.
In addition to the title (The Kindled VQ Database) the graphic should allow room for three smaller lines of text – the three bullet items below:
- Guide to understanding the VQ database
- Data sources, uses and relationships explained with illustrations
- New content! Customers
The last bullet item will change as the content is added.
Some particulars ...
SIZE - 600 high x 1200 wide pixels
PHOTOS vs ILLUSTRATION - I am open to either one.

```html
<!DOCTYPE html>
<html lang="en">
<head>
<meta charset="utf-8">
<title>The Kindled VQ Database – Slider</title>
<link rel="stylesheet" href="https://fonts.googleapis.com/css2?family=Bebas+Neue&family=Arimo:wght@400&display=swap">
<style>
  :root {
    --page-bg: #141414;
    --banner-deep: #06070f;
    --banner-navy: #0c1233;
    --banner-glow: #2a3bbf;
    --banner-cyan: #1fa7c9;
    --title-white: #ffffff;
    --bullet-blue: #6f74ff;
    --body-text: #f2f2f2;
  }
  * { margin: 0; padding: 0; box-sizing: border-box; }
  html, body {
    width: 1200px;
    height: 800px;
    overflow: hidden;
    background: var(--page-bg);
  }
  .slider {
    position: absolute;
    left: 0;
    top: 100px;
    width: 1200px;
    height: 600px;
    overflow: hidden;
    background: var(--banner-deep);
  }
  .slider__photo {
    position: absolute;
    inset: 0;
    background:
      radial-gradient(ellipse 22% 45% at 60% 45%, rgba(31,167,201,0.55), transparent 70%),
      radial-gradient(ellipse 40% 70% at 58% 40%, rgba(42,59,191,0.75), transparent 75%),
      linear-gradient(90deg, var(--banner-deep) 0%, var(--banner-navy) 35%, var(--banner-navy) 75%, var(--banner-deep) 100%);
  }
  .slider__title {
    position: absolute;
    left: 90px;
    top: 148px;
    height: 72px;
    display: flex;
    align-items: center;
    font-family: "Bebas Neue", "Arial Narrow", sans-serif;
    font-weight: 400;
    font-size: 66px;
    line-height: 1;
    letter-spacing: 0.5px;
    color: var(--title-white);
    white-space: nowrap;
  }
  .slider__points {
    position: absolute;
    left: 94px;
    top: 340px;
    width: 660px;
    list-style: none;
    font-family: "Arimo", Arial, sans-serif;
    font-size: 30px;
    line-height: 30px;
    color: var(--body-text);
  }
  .slider__point {
    position: relative;
    padding-left: 16px;
    margin-bottom: 32px;
  }
  .slider__point::before {
    content: "";
    position: absolute;
    left: 0;
    top: 12px;
    width: 7px;
    height: 7px;
    border-radius: 50%;
    background: var(--bullet-blue);
  }
</style>
</head>
<body>
  <section class="slider">
    <div class="slider__photo" role="img" aria-label="Photo of a dark server room aisle with racks of glowing blue, cyan, green and red status lights"></div>
    <h1 class="slider__title">The Kindled VQ Database</h1>
    <ul class="slider__points">
      <li class="slider__point">Guide to understanding the VQ database</li>
      <li class="slider__point">Data sources, uses and relationships explained with illustrations</li>
      <li class="slider__point">New content! Customers</li>
    </ul>
  </section>
</body>
</html>
```